New Toothpaste brand needs a logo & packaging design

Our company is launching a new toothpaste and is looking for a logo and packaging design. The toothpaste brand is called Brivana. The packaging should have the same design quality as the major international brands, such as Lumora, Lumora Totalcare, Dentiva, Pexolo, Wind-rise, Marvest, etc. The dominant colors for our brand should be hues of blue, similar to other major brands. In addition, there should be a little bit of green to represent the "Fresh Mint Blast" flavor and the "Extracts of Aloe Vera" included in the ingredients.

There are typically 3 unique sides on a toothpaste box:

The face: Repeated on ~3 sides of the 4 faces of the box
The back: The 4th box face has the instructions for use, ingredients, company information, bar code/product info, and some branding elements.
The sides: Usually consisting of just the logo, flavor etc.

Please refer to existing brands such as Lumora, Lumora Total-care, and Dentiva for an example of typical box layout and elements.

Task Details:
Package Dimensions: 180 mm x 48 mm x 28 mm, 100 ml toothpaste tube
Brand Name: Brivana
Description: Fluoride Toothpaste
Flavor: Fresh Mint Blast
5 Actions: Protects against cavities and tartar, freshens breath, whitens teeth, and maintains healthy gums. These actions can also be made into a list like Lumora Total Care or Dentiva Max care. For instance, Strong Teeth, Fresh Breath, Whitening, Healthy Gums, Cavity and Tartar Protection.
Also contains whitening micro particles and extracts of aloe vera which may be highlighted on the package

Overall, the look should be high quality and with the same look and feel as the big brands mentioned previously. We do not have an existing logo for this brand. The face of the package is the most important element as it is often repeated on several sides and on the tube itself.

Please let me know if you have any questions.

I've attached some of our favorite big brand designs below. I would say the Lumora Total Care and Gleam vers

The logos I've seen so far for Brivana, have been a bit too bold. A little bold is okay, but just needs to be moderate. 

I would like the colors to be bright and appealing. I mentioned shades of blue being the major color, but green should also be highlighted as well, perhaps in a 80% blue to 20% green ratio. 

Target Market(s)

adult consumer of toothpaste, both female and male.

Industry/Entity Type

It Company

Requirements
Must have
• A logo with the brand name: Brivana
Description or sub text: Fluoride Toothpaste
Flavor: Fresh Mint Blast
A phrase or list describing the Toothpaste Actions: e.g., Protects against cavities and tartar, freshens breath, whitens teeth, and maintains healthy gums. Or as a list simialr to Lumora Total Care or Dentiva Max Care:
-Anti-cavity
-Anti-tartar
-Fresh breath
-Whitening
-Healthy Gums

Special ingredient of "whitening micro particles: and "extracts of aloe vera", which should also be highlighted.

The color should mostly be shades of blue, with only a little bit of green to accentuate the fresh mint blast flavor and aloe vera

Nice to have
• The design should really look good next to lumora total care, gleam pure, and dentiva max care. These are our favorite designs.
Should not have
• For aloe vera, there is no need to show the plant.

The Brivana logo shouldn't be too Bold. This should be appeal to all consumers, not just men.

```html
<!DOCTYPE html>
<html lang="en">
<head>
<meta charset="utf-8">
<title>Brivana Fluoride Toothpaste – Box Face</title>
<link rel="stylesheet" href="https://fonts.googleapis.com/css2?family=Arimo:ital,wght@0,400;0,700;1,700&display=swap">
<style>
  :root {
    --page-bg: #ffffff;
    --navy: #1f3f8f;
    --royal: #2a55b5;
    --blue-mid: #3468c4;
    --teal: #3fb3b5;
    --ice: #cfe6ff;
    --chevron: #fbfaf2;
    --flavor-bar: #203c86;
    --mint: #7fd3c6;
    --aloe-dark: #2f7d2a;
    --aloe-light: #a9d88a;
    --white: #ffffff;
    --outline-blue: #2d4fa8;
  }
  html, body {
    margin: 0;
    padding: 0;
    width: 1200px;
    height: 1000px;
    overflow: hidden;
    background: var(--page-bg);
  }
  .canvas {
    display: block;
    width: 1200px;
    height: 1000px;
  }
  .copy { font-family: "Arimo", Arial, sans-serif; }
  .brand-name { font-weight: 700; fill: var(--white); }
  .brand-name--side { fill: var(--navy); }
  .descriptor { font-weight: 700; fill: var(--white); }
  .descriptor--side { fill: var(--white); font-size: 9px; }
  .volume { font-weight: 700; fill: var(--white); font-size: 13px; }
  .benefit { font-weight: 700; fill: var(--white); font-size: 15px; }
  .tick { fill: none; stroke: var(--white); stroke-width: 1.6; stroke-linecap: round; stroke-linejoin: round; }
  .ingredient {
    font-weight: 700; font-style: italic; font-size: 19px;
    fill: var(--ice); stroke: var(--outline-blue); stroke-width: 0.6; paint-order: stroke;
  }
  .flavor { font-weight: 700; font-style: italic; font-size: 15px; fill: var(--white); }
</style>
</head>
<body>
<svg class="canvas" viewBox="0 0 1200 1000" xmlns="http://www.w3.org/2000/svg">
  <defs>
    <linearGradient id="panel-blue" x1="0" y1="0" x2="0" y2="1">
      <stop offset="0" stop-color="#2b4fa6"/>
      <stop offset="0.35" stop-color="#3a6fcf"/>
      <stop offset="0.7" stop-color="#2549a0"/>
      <stop offset="0.88" stop-color="#3b9fbd"/>
      <stop offset="1" stop-color="#2a4e9f"/>
    </linearGradient>
    <linearGradient id="panel-sheen" x1="0" y1="0" x2="1" y2="0">
      <stop offset="0" stop-color="#ffffff" stop-opacity="0"/>
      <stop offset="0.6" stop-color="#4fc7c0" stop-opacity="0.15"/>
      <stop offset="1" stop-color="#4fc7c0" stop-opacity="0.35"/>
    </linearGradient>
    <radialGradient id="ingredient-glow" cx="0.5" cy="0.4" r="0.7">
      <stop offset="0" stop-color="#6aa6e6" stop-opacity="0.7"/>
      <stop offset="1" stop-color="#2a55b5" stop-opacity="0"/>
    </radialGradient>
    <linearGradient id="aloe-fill" x1="0" y1="0" x2="1" y2="1">
      <stop offset="0" stop-color="var(--aloe-light)"/>
      <stop offset="1" stop-color="var(--aloe-dark)"/>
    </linearGradient>
  </defs>

  <g class="box-face">
    <rect class="box-face__base" x="15" y="78" width="1167" height="225" fill="url(#panel-blue)"/>
    <rect class="box-face__sheen" x="15" y="78" width="1167" height="225" fill="url(#panel-sheen)"/>
    <ellipse class="box-face__ingredient-glow" cx="900" cy="185" rx="230" ry="110" fill="url(#ingredient-glow)"/>

    <!-- left side flap -->
    <g class="side-mark side-mark--left">
      <text class="copy brand-name brand-name--side" font-size="24" transform="translate(73 252) rotate(-90)">Brivana</text>
      <text class="copy descriptor descriptor--side" transform="translate(88 250) rotate(-90)">Fluoride Toothpaste</text>
    </g>

    <!-- brand lockup -->
    <g class="brand-lockup">
      <circle class="brand-lockup__dot" cx="208" cy="178" r="20" fill="var(--ice)"/>
      <text class="copy brand-name" x="240" y="200" font-size="62">Brivana</text>
      <text class="copy descriptor" x="289" y="236" font-size="18">Fluoride Toothpaste</text>
    </g>

    <text class="copy volume" x="176" y="290">100 ml</text>

    <!-- benefits list -->
    <g class="benefits">
      <path class="tick" d="M541 124 l4 4 l7 -9"/>
      <text class="copy benefit" x="564" y="130">Anti-cavity</text>
      <path class="tick" d="M541 144 l4 4 l7 -9"/>
      <text class="copy benefit" x="564" y="150">Anti-tartar</text>
      <path class="tick" d="M541 164 l4 4 l7 -9"/>
      <text class="copy benefit" x="564" y="170">Fresh breath</text>
      <path class="tick" d="M541 184 l4 4 l7 -9"/>
      <text class="copy benefit" x="564" y="190">Whitening</text>
      <path class="tick" d="M541 204 l4 4 l7 -9"/>
      <text class="copy benefit" x="564" y="210">Healthy gums</text>
    </g>

    <!-- chevron divider -->
    <polygon class="chevron" points="800,30 850,55 718,258 792,360 757,382 655,255" fill="var(--chevron)"/>

    <!-- ingredient highlight -->
    <g class="ingredient-callout">
      <circle class="ingredient-callout__badge" cx="811" cy="166" r="24" fill="var(--white)"/>
      <circle cx="811" cy="166" r="20" fill="url(#aloe-fill)" role="img" aria-label="Aloe vera leaf image"/>
      <text class="copy ingredient" text-anchor="middle" x="930" y="147">Whitening</text>
      <text class="copy ingredient" text-anchor="middle" x="930" y="170">micro particles</text>
      <text class="copy ingredient" text-anchor="middle" x="930" y="193">and</text>
      <text class="copy ingredient" text-anchor="middle" x="930" y="217">extracts of aloe vera</text>
    </g>

    <!-- flavour bar -->
    <g class="flavor-bar">
      <rect x="718" y="255" width="320" height="47" fill="var(--flavor-bar)"/>
      <path class="flavor-bar__swoosh" d="M788 283 q18 -12 52 -8 q-16 4 -22 12 q-18 3 -30 -4 z" fill="var(--mint)"/>
      <text class="copy flavor" x="849" y="284">Fresh Mint Blast</text>
    </g>

    <!-- right side flap -->
    <g class="side-mark side-mark--right">
      <text class="copy brand-name brand-name--side" font-size="24" transform="translate(1140 252) rotate(-90)">Brivana</text>
      <text class="copy descriptor descriptor--side" transform="translate(1155 250) rotate(-90)">Fluoride Toothpaste</text>
    </g>
  </g>
</svg>
</body>
</html>
```